Menu Design Project

Bel Roux hair and beauty service menu
we need a menu to display a handful of our services to give our customers an idea of our pricing

Cutting
Ladies cuts from $35
Men's cuts from $25
All cuts are included with a wash and dry off

Velora colours
All over colours start from $55
price will vary depending upon length and thickness of hair

Foiling
starts from $50
Price will vary depending upon length of hair

Toners
from $30

Blowdries
from $35

Upstyling
wedding styling from $45
Please enquire for special occasion styling also

Beauty Services

Waxing
Eyebrow wax and shape $17.50
Lip $10
Chin/sides $20
Legs from $25
Bikini $20
XX $30
XXX $45
Back from $25
Chest from $25

Eyes
Eyebrow tinting $15
Eyelash tinting $20
Eyelash extensions from $90

Derminia facials
Express facial $45
Deluxe facial $95

Acrylic nails
full set $60
Gel polish $35
Manicures from $35
Pedicures from $45

can provide logo and other images to help

Industry/Entity Type

Hair

Requirements
Must have
• must be called a service menu
must be eye catching and memorable but not excessive
Nice to have
• postcard style size hair menu on one side
beauty menu on the other side
elegant classy design
Should not have
• must not be called a price list
stay away from traditional price list style in terms of folding out leaflet

```html
<!DOCTYPE html>
<html lang="en">
<head>
<meta charset="utf-8">
<title>Bel Roux Service menu</title>
<link rel="stylesheet" href="https://fonts.googleapis.com/css2?family=Inter:wght@200;300;400&display=swap">
<style>
  :root {
    --paper: #ffffff;
    --ink: #1a1a1a;
    --ink-soft: #555555;
    --hair-light: #d9c6a8;
    --hair-mid: #a88a66;
    --hair-dark: #5e4632;
    --skin: #e9c2a6;
  }
  html, body {
    margin: 0;
    padding: 0;
    overflow: hidden;
    background: var(--paper);
  }
  .menu-card {
    position: relative;
    width: 1200px;
    height: 866px;
    background: var(--paper);
    font-family: "Inter", Helvetica, Arial, sans-serif;
    color: var(--ink);
    overflow: hidden;
  }
  .menu-title {
    position: absolute;
    left: 164px;
    top: 84px;
    margin: 0;
    font-size: 41px;
    font-weight: 200;
    letter-spacing: -0.5px;
  }
  .service-list {
    position: absolute;
    left: 165px;
    top: 158px;
    width: 424px;
  }
  .service {
    margin-bottom: 20px;
  }
  .service-name {
    margin: 0;
    font-size: 22px;
    font-weight: 300;
    line-height: 30px;
  }
  .price-row {
    display: flex;
    justify-content: space-between;
    align-items: baseline;
    font-size: 23px;
    font-weight: 200;
    line-height: 29px;
    color: var(--ink-soft);
  }
  .price {
    font-size: 14px;
    font-weight: 300;
    color: var(--ink);
  }
  .service-note {
    font-size: 13px;
    font-weight: 300;
    color: var(--ink-soft);
    line-height: 16px;
    letter-spacing: -0.2px;
  }
  .section-label {
    position: absolute;
    left: 56px;
    top: 785px;
    transform: rotate(-90deg);
    transform-origin: left top;
    margin: 0;
    font-size: 58px;
    font-weight: 200;
    line-height: 1;
  }
  .hero-photo {
    position: absolute;
    left: 615px;
    top: 0;
    width: 585px;
    height: 866px;
    background:
      radial-gradient(ellipse at 78% 78%, var(--skin) 0%, rgba(233,194,166,0) 45%),
      radial-gradient(ellipse at 45% 35%, var(--hair-light) 0%, var(--hair-mid) 45%, rgba(94,70,50,0.6) 70%, rgba(255,255,255,0) 90%);
  }
</style>
</head>
<body>
<main class="menu-card">
  <h1 class="menu-title">Bel Roux Service menu</h1>

  <section class="service-list">
    <div class="service">
      <h2 class="service-name">Cuts</h2>
      <div class="price-row"><span>Ladies cuts from</span><span class="price">$35</span></div>
      <div class="price-row"><span>Men’s cuts from</span><span class="price">$25</span></div>
      <div class="service-note">All cuts are included with a wash and dry off</div>
    </div>
    <div class="service">
      <h2 class="service-name">Velora colours</h2>
      <div class="price-row"><span>All over colours start from</span><span class="price">$55</span></div>
      <div class="service-note">Price will vary depending upon length and thickness of hair</div>
    </div>
    <div class="service">
      <h2 class="service-name">Foiling</h2>
      <div class="price-row"><span>starts from</span><span class="price">$50</span></div>
      <div class="service-note">Price will vary depending upon length of hair</div>
    </div>
    <div class="service">
      <h2 class="service-name">Toners</h2>
      <div class="price-row"><span>from</span><span class="price">$30</span></div>
    </div>
    <div class="service">
      <h2 class="service-name">Blowdries</h2>
      <div class="price-row"><span>from</span><span class="price">$35</span></div>
      <div class="service-note">Price will vary depending upon length and thickness of hair</div>
    </div>
    <div class="service">
      <h2 class="service-name">Upstyling</h2>
      <div class="price-row"><span>wedding styling from</span><span class="price">$45</span></div>
      <div class="service-note">Please enquire for special occasion styling also</div>
    </div>
  </section>

  <p class="section-label">Cutting</p>

  <div class="hero-photo" role="img" aria-label="Photo of a model with tousled blonde highlighted hair and a fringe"></div>
</main>
</body>
</html>
```